Start out business card needed

We have uploaded a flyer we like the design of for inspiration for the business card.

Target Market(s)

Fitness lovers

Industry/Entity Type

Health And Wellness

Contact Information for Business Card

Business Development Manager
Mick de la porte
Phone number to be advised
Mick@lift-yard.com.au
www.lift-yard.com.au

Font styles to use
Sans Serif

Colors
fbee3e
1b1b1b
f5f5f5

Requirements
Must have
• Front : Logo (large should take up most of the space)
• Back : small logo, business details

```html
<!DOCTYPE html>
<html lang="en">
<head>
<meta charset="utf-8">
<title>Lift Yard – Business Card</title>
<link rel="stylesheet" href="https://fonts.googleapis.com/css2?family=Open+Sans:wght@400;600;700&family=Oswald:wght@500&display=swap">
<style>
  :root {
    --yellow: #fbee3e;
    --gold: #f2c200;
    --ink: #1b1b1b;
    --charcoal: #2f2f30;
    --paper: #f5f5f5;
    --stage: #66758b;
    --muted: #c9c9c9;
  }
  * { box-sizing: border-box; margin: 0; padding: 0; }
  html, body { width: 1200px; height: 810px; overflow: hidden; }
  body {
    background: var(--stage);
    font-family: "Open Sans", Arial, sans-serif;
    display: flex;
    flex-direction: column;
    align-items: center;
    justify-content: center;
    gap: 50px;
  }
  .card {
    position: relative;
    width: 600px;
    height: 343px;
    background: var(--paper);
    overflow: hidden;
    box-shadow: 0 10px 24px rgba(0,0,0,.28);
  }
  .card-shape { position: absolute; inset: 0; width: 100%; height: 100%; }
  .brand {
    position: absolute;
    font-family: "Oswald", "Arial Narrow", sans-serif;
    font-weight: 500;
    color: var(--ink);
    letter-spacing: .12em;
    white-space: nowrap;
  }
  .card-front .brand { right: 32px; top: 50%; transform: translateY(-50%); font-size: 48px; }
  .card-back .brand { right: 40px; top: 50%; transform: translateY(-50%); font-size: 30px; }
  .details { position: absolute; left: 34px; top: 34px; color: var(--paper); }
  .name { font-size: 23px; font-weight: 700; line-height: 1.1; }
  .role { font-size: 11.5px; color: var(--muted); margin-top: 4px; letter-spacing: .02em; }
  .contact-list { list-style: none; margin-top: 40px; }
  .contact-list li {
    display: flex; align-items: center; gap: 10px;
    font-size: 11.5px; line-height: 1.35; margin-bottom: 9px;
  }
  .contact-list svg { flex: none; width: 13px; height: 13px; }
</style>
</head>
<body>

<section class="card card-front" aria-label="Card front">
  <svg class="card-shape" viewBox="0 0 600 343" aria-hidden="true">
    <defs>
      <linearGradient id="darkSweep" x1="0" y1="0" x2="1" y2="1">
        <stop offset="0" stop-color="#3a3a3b"/>
        <stop offset=".55" stop-color="#232324"/>
        <stop offset="1" stop-color="#1b1b1b"/>
      </linearGradient>
    </defs>
    <path d="M0 0 H300 Q215 171 300 343 H0 Z" fill="url(#darkSweep)"/>
    <path d="M300 0 Q215 171 300 343" fill="none" stroke="var(--gold)" stroke-width="9"/>
  </svg>
  <div class="brand">LIFT YARD</div>
</section>

<section class="card card-back" aria-label="Card back">
  <svg class="card-shape" viewBox="0 0 600 343" aria-hidden="true">
    <defs>
      <linearGradient id="backDark" x1="0" y1="0" x2="1" y2="0">
        <stop offset="0" stop-color="#2a2a2b"/>
        <stop offset="1" stop-color="#3b3b3c"/>
      </linearGradient>
    </defs>
    <path d="M0 0 H380 Q300 171 380 343 H0 Z" fill="url(#backDark)"/>
    <path d="M380 0 Q300 171 380 343" fill="none" stroke="var(--gold)" stroke-width="7"/>
  </svg>
  <svg class="card-shape" viewBox="0 0 600 343" role="img" aria-label="Black and white photo of an athlete's arm with a wrist wrap">
    <defs>
      <linearGradient id="photoTone" x1="0" y1="0" x2="0" y2="1">
        <stop offset="0" stop-color="#8a8a8a" stop-opacity=".45"/>
        <stop offset="1" stop-color="#8a8a8a" stop-opacity="0"/>
      </linearGradient>
    </defs>
    <path d="M0 0 H380 Q355 55 352 120 H0 Z" fill="url(#photoTone)"/>
  </svg>
  <div class="details">
    <div class="name">Mick de la porte</div>
    <div class="role">Business Development Manager</div>
    <ul class="contact-list">
      <li>
        <svg viewBox="0 0 12 12"><path d="M6 0.5a4 4 0 0 0-4 4c0 3 4 7 4 7s4-4 4-7a4 4 0 0 0-4-4zm0 5.5a1.5 1.5 0 1 1 0-3 1.5 1.5 0 0 1 0 3z" fill="var(--yellow)"/></svg>
        <span>410 Harbor Point Rd, Ste 12,<br>Seaside, CA 90210</span>
      </li>
      <li>
        <svg viewBox="0 0 12 12"><path d="M2.5 1 L4.5 1 L5.3 3.5 L4 4.5 Q5 7 7.5 8 L8.5 6.7 L11 7.5 L11 9.5 Q11 11 9.5 11 Q1 10.5 1 2.5 Q1 1 2.5 1Z" fill="var(--yellow)"/></svg>
        <span>555 010 2471</span>
      </li>
      <li>
        <svg viewBox="0 0 12 12"><rect x="0.5" y="2" width="11" height="8" rx="1" fill="var(--yellow)"/><path d="M1 2.6 L6 6.5 L11 2.6" fill="none" stroke="var(--ink)" stroke-width="1"/></svg>
        <span>Mick@lift-yard.com.au</span>
      </li>
      <li>
        <svg viewBox="0 0 12 12"><circle cx="6" cy="6" r="5" fill="none" stroke="var(--yellow)" stroke-width="1.2"/><path d="M1 6 H11 M6 1 Q3 6 6 11 Q9 6 6 1" fill="none" stroke="var(--yellow)" stroke-width="1"/></svg>
        <span>www.lift-yard.com.au</span>
      </li>
    </ul>
  </div>
  <div class="brand">LIFT YARD</div>
</section>

</body>
</html>
```